New audiology website PSD design only - guaranteed

We need a clean and attractive website to replace an existing Audiology (hearing technology) website which will be wordpress based.
The current website is: http://pelmorahearing.com.au
They have a new logo and colors which you can find at www.quodel.net/temp/plh2018.pdf
We will no longer have a web shop in the new website
To enter the competition, we only need a sample of the home page.
The winning design will be asked to produce 2 standard page template alternatives as well (based on the winning home page design, but for a standard page layout)
The winning design must provide any photos used
We want a clean, credible site but with some warmth
Target Market(s)
All ages but needs to include the elderly
Industry/Entity Type
Medical And Science
Number of Pages Required
3 page
Look and feel
Each slider illustrates characteristics of the customer's brand and the style your logo design should communicate.

```html
<!DOCTYPE html>
<html lang="en">
<head>
<meta charset="utf-8">
<title>Pelmora Hearing – Home</title>
<link href="https://fonts.googleapis.com/css2?family=Roboto:ital,wght@0,300;0,400;0,500;0,700;0,900;1,400&display=swap" rel="stylesheet">
<style>
:root{
  --orange:#f07b2c;
  --charcoal:#2c2c2c;
  --text:#333333;
  --white:#ffffff;
  --grey-panel:#c9c9c9;
  --field:#ffffff;
}
*{box-sizing:border-box;margin:0;padding:0}
html,body{width:1200px;height:4918px;overflow:hidden}
body{font-family:"Roboto",sans-serif;color:var(--text);background:var(--white);position:relative}
.section{position:absolute;left:0;width:1200px;overflow:hidden}
.btn{display:inline-block;border:2px solid var(--orange);color:var(--orange);border-radius:40px;padding:11px 24px;font-size:24px;font-weight:300;letter-spacing:.5px;background:transparent;line-height:1.2}
.btn-light{border-color:var(--white);color:var(--white)}
.btn-solid{background:var(--orange);color:var(--white)}
.body-copy{font-size:19px;line-height:1.35;font-weight:400}

/* header */
.site-header{top:0;height:98px;background:linear-gradient(#2a2a2a,#3a3a3a);z-index:5;overflow:visible}
.logo-tab{position:absolute;left:0;top:0;width:430px;height:112px;background:var(--white);border-radius:0 0 70px 0;display:flex;align-items:center;padding-left:40px;gap:14px}
.logo-dot{width:52px;height:52px;border-radius:50%;background:var(--orange);flex:none}
.logo-name{font-size:40px;font-weight:500;color:var(--charcoal);white-space:nowrap}
.phone{position:absolute;left:520px;top:6px;color:var(--orange);font-size:22px;font-weight:700;display:flex;align-items:center;gap:10px}
.login{position:absolute;left:790px;top:6px;display:flex;gap:10px;align-items:center}
.login-field{width:140px;height:26px;background:var(--white);border-radius:14px;font-size:13px;color:#999;padding:5px 12px}
.login-go{background:var(--orange);color:var(--white);border-radius:14px;font-size:13px;font-weight:700;padding:5px 14px}
.login-help{position:absolute;right:30px;top:38px;font-size:12px;color:var(--orange)}
.main-nav{position:absolute;right:30px;top:60px;display:flex;gap:22px;font-size:17px;color:var(--orange)}

/* hero */
.hero{top:0;height:760px}
.hero-photo{position:absolute;inset:0;background:linear-gradient(180deg,#bcd7e6 0%,#8fb9cf 45%,#c6aa8c 75%,#e7d2bd 100%)}
.hero-panel{position:absolute;left:620px;top:200px;width:580px;height:420px;background:rgba(255,255,255,.78);border-radius:50px 0 0 50px;padding:36px 40px}
.hero-panel .kicker{font-size:36px;color:var(--orange);font-weight:300;line-height:1.1}
.hero-panel h1{font-size:54px;font-weight:900;color:var(--orange);line-height:1.05;margin-bottom:14px;white-space:nowrap}
.hero-panel p{font-size:20px;line-height:1.35;margin-bottom:18px}
.hero-panel .btn{float:right}
.hero-curve{position:absolute;left:0;top:560px}

/* hearing aids */
.hearing-aids{top:760px;height:824px}
.hearing-aids h2{position:absolute;left:52px;top:128px;font-size:58px;font-weight:900;color:var(--orange)}
.hearing-aids .body-copy{position:absolute;left:52px;top:212px;width:580px}
.hearing-aids .body-copy p{margin-bottom:24px}
.hearing-aids .btn{position:absolute;left:52px;top:505px}
.hand-photo{position:absolute;left:300px;top:420px;width:900px;height:380px;background:radial-gradient(ellipse at 55% 55%,#f0d0bb 0%,#e3b79d 40%,#ffffff 75%)}

/* treatments */
.treatments{top:1584px;height:786px;background:var(--orange)}
.treatments .text{position:absolute;left:52px;top:66px;width:540px;color:var(--white)}
.treatments .small-head{font-size:38px;font-weight:300}
.treatments h2{font-size:56px;font-weight:900;line-height:1;margin-bottom:16px}
.treatments p{margin-bottom:22px}
.otoscope-photo{position:absolute;left:615px;top:0;width:585px;height:786px;background:linear-gradient(135deg,#f3e3d8 0%,#e2c2ae 45%,#9b9b9b 70%,#d8c1b4 100%)}

/* music */
.music{top:2370px;height:904px}
.music-photo{position:absolute;inset:0;background:linear-gradient(90deg,#5a4a3c 0%,#8a7560 45%,#c6b9a8 70%,#7a6a5a 100%)}
.music-panel{position:absolute;left:130px;top:160px;width:720px;height:600px;background:rgba(255,255,255,.78);border-radius:60px;padding:40px 60px}
.music-panel h2{font-size:56px;font-weight:900;color:var(--orange);margin-bottom:18px}
.music-panel p{font-size:20px;line-height:1.33}
.music-panel .btn{margin-top:22px}

/* contact */
.contact{top:3274px;height:850px}
.contact h2{position:absolute;left:0;width:1200px;top:100px;text-align:center;font-size:52px;font-weight:700;color:var(--orange)}
.contact .intro{position:absolute;left:110px;width:980px;top:168px;text-align:center;font-size:20px;line-height:1.35}
.form-panel{position:absolute;left:115px;top:228px;width:965px;height:640px;background:var(--grey-panel);border-radius:60px 60px 0 0}
.form-panel .note{position:absolute;top:16px;width:100%;text-align:center;font-size:18px;color:var(--white)}
.field{position:absolute;background:var(--field);border-radius:24px;font-size:19px;font-style:italic;color:#999;padding:13px 22px;height:50px}
.form-buttons{position:absolute;left:410px;top:535px;display:flex;gap:30px}
.form-buttons .btn{font-size:20px;font-weight:500;padding:12px 50px;background:#f1f1f1}
.form-buttons .btn-solid{background:var(--orange)}

/* urgent */
.urgent{top:4114px;height:658px;background:var(--orange);border-radius:110px 110px 0 0;color:var(--white)}
.urgent h2{position:absolute;left:52px;top:66px;font-size:54px;font-weight:900}
.urgent .intro{position:absolute;left:52px;top:145px;font-size:20px}
.location{position:absolute;top:200px;width:440px;font-size:18px;line-height:1.35}
.location h3{font-size:20px;font-weight:700}
.location address{font-style:italic}
.location .tel{font-weight:700;font-size:21px;margin:22px 0 8px}
.map{width:380px;height:230px;background:linear-gradient(135deg,#e9e4da,#d6dfcc 50%,#f0eadb)}

/* footer */
.site-footer{top:4772px;height:146px;background:linear-gradient(#3a3a3a,#222)}
.footer-logo{position:absolute;left:40px;top:45px;display:flex;align-items:center;gap:14px}
.footer-logo .logo-dot{width:56px;height:56px}
.footer-logo .logo-name{color:var(--white);font-size:46px}
.footer-links{position:absolute;right:52px;top:40px;text-align:right;color:var(--white);font-size:20px;line-height:1.5}
.footer-links strong{font-weight:700}
</style>
</head>
<body>

<header class="section site-header">
  <div class="logo-tab"><span class="logo-dot"></span><span class="logo-name">Pelmora Hearing</span></div>
  <div class="phone">
    <svg width="22" height="22" viewBox="0 0 24 24"><path fill="#f07b2c" d="M6.6 10.8c1.4 2.8 3.8 5.1 6.6 6.6l2.2-2.2c.3-.3.7-.4 1-.2 1.1.4 2.3.6 3.6.6.6 0 1 .4 1 1V20c0 .6-.4 1-1 1C10.6 21 3 13.4 3 4c0-.6.4-1 1-1h3.5c.6 0 1 .4 1 1 0 1.3.2 2.5.6 3.6.1.3 0 .7-.2 1L6.6 10.8z"/></svg>
    (02) 9000 4127
  </div>
  <div class="login"><span class="login-field">Username</span><span class="login-field">Password</span><span class="login-go">LOG IN</span></div>
  <div class="login-help">Forgot password? &nbsp; Not registered?</div>
  <nav class="main-nav"><span>Home</span><span>About Us</span><span>Hearing Aids</span><span>Doctor's Information</span><span>Musicians</span><span>Contact</span></nav>
</header>

<section class="section hero">
  <div class="hero-photo" role="img" aria-label="Photo of a woman holding a seashell to her ear on a beach"></div>
  <svg class="hero-curve" width="1200" height="200" viewBox="0 0 1200 200">
    <path d="M0 40 Q600 230 1200 40 L1200 200 L0 200Z" fill="#fff"/>
    <path d="M430 130 L600 190 L770 130" fill="none" stroke="#fff" stroke-opacity=".6" stroke-width="6"/>
  </svg>
  <div class="hero-panel">
    <div class="kicker">Rediscover the</div>
    <h1>WORLD OF SOUND</h1>
    <p>Pelmora Hearing is an independently owned and managed professional audiology clinic. Our Audiologists are health-care professionals specialising in diagnosing, treating and monitoring everything to do with hearing and balance.</p>
    <span class="btn">LEARN MORE</span>
  </div>
</section>

<section class="section hearing-aids">
  <div class="hand-photo" role="img" aria-label="Photo of an open hand holding a small hearing aid"></div>
  <h2>HEARING AIDS</h2>
  <div class="body-copy">
    <p>When considering a hearing aid it is important that you understand your hearing loss and your expectations of a hearing aid. There may be several hearing aids that are appropriate to your hearing loss, but there may only be one or two that comfortably fit the shape of your ear and successfully fit in with your life style.</p>
    <p>As we are a truly independent clinic, we have the latest hearing aids from all leading manufacturers at the most competitive prices.</p>
  </div>
  <span class="btn">LEARN MORE</span>
</section>

<section class="section treatments">
  <div class="text body-copy">
    <div class="small-head">BEST TREATMENTS</div>
    <h2>ENSURED!</h2>
    <p>Pelmora Hearing is one of Sydney's leading diagnostic hearing and balance clinics. Referring doctors can be assured that all testing and rehabilitation is reviewed to the highest industry standards. Our Audiologists also work closely with referring ENT's and Doctors to ensure all testing meets the needs of their practice.</p>
    <p>Pelmora Hearing are fully accredited with the Hearing Care Office (HCO), all pensioners with an HCO voucher receive a hearing assessment, consultation, hearing aids (if applicable) and ongoing rehabilitation services with no out of pocket expenses.</p>
    <p>Pelmora Hearing is also Worksure accredited and supplies the latest hearing aids from all the leading manufacturers.</p>
    <span class="btn btn-light">LEARN MORE</span>
  </div>
  <div class="otoscope-photo" role="img" aria-label="Photo of an otoscope examining an ear"></div>
</section>

<section class="section music">
  <div class="music-photo" role="img" aria-label="Photo of a young woman with in-ear monitors in front of a guitar background"></div>
  <div class="music-panel">
    <h2>FOR MUSIC LOVERS!</h2>
    <p>If you are a professional musician, audiophile, TV/Radio presenter, amateur musician or just casually listen to tunes on your MP3 player you should have custom moulded in ear monitors (IEM's).<br>Our Audiologists can take professional ear impressions for your custom fit In Ear Monitors. So if you see a range of IEM's online that we don't stock and you need ear impressions to send away, you can be confident that we can take ear impressions that will ensure you get a perfect acoustic seal.</p>
    <span class="btn">LEARN MORE</span>
  </div>
</section>

<section class="section contact">
  <h2>Get In Touch!</h2>
  <p class="intro">We are available to assist you with your queries. You can fill in the form below and we will get back to you as soon as possible.</p>
  <form class="form-panel">
    <div class="note">Fields marked with * are required.</div>
    <div class="field" style="left:213px;top:60px;width:535px">*Full Name</div>
    <div class="field" style="left:213px;top:128px;width:255px">*Email</div>
    <div class="field" style="left:493px;top:128px;width:255px">Phone Number</div>
    <div class="field" style="left:213px;top:196px;width:535px">*Subject</div>
    <div class="field" style="left:213px;top:264px;width:535px;height:250px;border-radius:28px">*Message</div>
    <div class="form-buttons"><span class="btn">RESET</span><span class="btn btn-solid">SUBMIT</span></div>
  </form>
</section>

<section class="section urgent">
  <h2>URGENT QUERIES?</h2>
  <p class="intro">You can contact us at any of the locations below <strong>Monday to Friday</strong> between <strong>9am to 5pm.</strong></p>
  <div class="location" style="left:52px">
    <h3>Kestrel Park</h3>
    <address>Ground Floor, Suite 4, 18 Harbour Road<br>Kestrel Park, NSW, 2061</address>
    <div class="tel">Phone: 9000 4127</div>
    <div class="map" role="img" aria-label="Street map of the Kestrel Park clinic"></div>
  </div>
  <div class="location" style="left:732px">
    <h3>Ferrow Bay</h3>
    <address>Shop 7, 42 Wattle Street<br>Ferrow Bay, NSW, 2044</address>
    <div class="tel">Phone: 9000 8836</div>
    <div class="map" role="img" aria-label="Street map of the Ferrow Bay clinic"></div>
  </div>
</section>

<footer class="section site-footer">
  <div class="footer-logo"><span class="logo-dot"></span><span class="logo-name">Pelmora Hearing</span></div>
  <div class="footer-links">
    <strong>© 2018, All Rights Reserved.</strong><br>
    Shipping and Refunds Policy | Terms and Conditions | Back to Top
  </div>
</footer>

</body>
</html>
```